Brochure Design For Beauty Salon

We have an existing brochure for our beauty salon business which has been designed in-house.

We need a designer to refresh the look and feel of the brochure, which is intended for print. The print format will be 210mmx210mm (square, stapled).

We need a design for each and every page of the brochure, including the front and back covers.

We are looking for a fresh modern design, quite close to what we already have, but looking more slick and professional.

The primary colors are white, grey and purple. The final design will communicate luxury, prestige and cleanliness and have a heavy focus on creating the feeling of space within each page.

Target Market(s)

Professional Women, aged 20-45

Industry/Entity Type

Beauty Salon

Font styles to use
Sans Serif
Other font styles liked:
• Helvetica

Requirements
Must have
• The project must be ready for print on square paper 210x210mm

```html
<!DOCTYPE html>
<html lang="en">
<head>
<meta charset="utf-8">
<title>Massage – Treatment Menu Spread</title>
<link href="https://fonts.googleapis.com/css2?family=Montserrat:wght@300;400;500;600&display=swap" rel="stylesheet">
<style>
  :root {
    --backdrop: #d4d4d4;
    --paper: #f7f7f7;
    --plum: #5e1034;
    --plum-dark: #4a0a28;
    --ink: #4a4a4a;
    --muted: #8a8a8a;
    --frame: #9a9a9a;
  }
  * { margin: 0; padding: 0; box-sizing: border-box; }
  html, body { width: 1200px; height: 801px; overflow: hidden; }
  body {
    background: var(--backdrop);
    font-family: "Montserrat", Helvetica, Arial, sans-serif;
    color: var(--ink);
  }
  .spread {
    position: absolute;
    left: 80px; top: 140px;
    width: 1040px; height: 520px;
    display: flex;
    box-shadow: 0 10px 30px rgba(0,0,0,0.18);
  }
  .page {
    position: relative;
    width: 520px; height: 520px;
    background: var(--paper);
    overflow: hidden;
  }
  .page--left { border-right: 1px solid #e2e2e2; }

  /* Left page */
  .intro-band {
    position: absolute;
    left: 0; top: 150px;
    width: 462px; height: 200px;
    background: linear-gradient(90deg, var(--plum-dark), var(--plum) 70%, #6d1d42);
  }
  .intro-frame {
    position: absolute;
    left: 72px; top: 72px;
    width: 376px; height: 376px;
    border: 1px solid var(--frame);
  }
  .intro-text {
    position: absolute;
    left: 72px; top: 172px;
    width: 376px;
    text-align: center;
    color: #fff;
  }
  .intro-title {
    font-weight: 300;
    font-size: 30px;
    letter-spacing: 2px;
  }
  .intro-rule {
    width: 44px; height: 1px;
    background: #fff;
    margin: 8px auto 14px;
  }
  .intro-copy {
    font-size: 9.5px;
    line-height: 1.45;
    padding: 0 18px;
    margin-bottom: 10px;
  }

  /* Right page */
  .top-swoosh { position: absolute; left: 0; top: 0; }
  .menu { position: absolute; left: 52px; top: 96px; width: 420px; }
  .menu-group { margin-bottom: 34px; }
  .menu-heading {
    font-weight: 600;
    font-size: 14px;
    color: var(--plum);
  }
  .menu-heading::after {
    content: "";
    display: block;
    width: 36px; height: 2px;
    background: var(--plum);
    margin: 4px 0 8px;
  }
  .menu-note {
    font-size: 7.5px;
    color: var(--muted);
    line-height: 1.4;
    margin-bottom: 6px;
  }
  .menu-row {
    display: flex;
    justify-content: space-between;
    font-size: 10.5px;
    line-height: 1.9;
  }
  .menu-price { color: var(--ink); }
  .menu-soon { font-size: 10px; margin-top: 4px; }
</style>
</head>
<body>
  <main class="spread">
    <section class="page page--left">
      <div class="intro-band"></div>
      <div class="intro-frame"></div>
      <div class="intro-text">
        <h1 class="intro-title">MASSAGE</h1>
        <div class="intro-rule"></div>
        <p class="intro-copy">You need a massage that combines the best techniques from around the world, using the finest oils and experienced, expert hands to leave you feeling brand new again. You need a Very Maren Signature massage.</p>
        <p class="intro-copy">Choose your ideal massage from our menu below. Each massage will be tailored to your needs which will be discussed before your treatment begins.</p>
      </div>
    </section>

    <section class="page page--right">
      <svg class="top-swoosh" width="520" height="110" viewBox="0 0 520 110">
        <path d="M0 92 C 120 70, 260 38, 420 22 L 520 14 L 520 0 L 430 0 C 280 18, 120 52, 0 72 Z" fill="var(--plum)"/>
      </svg>

      <div class="menu">
        <div class="menu-group">
          <h2 class="menu-heading">Eye Lift</h2>
          <div class="menu-row"><span>Signature Back, Neck and Shoulders</span><span class="menu-price">30 mins | £32.00</span></div>
          <div class="menu-row"><span>Signature Full Body</span><span class="menu-price">60 mins | £49.00</span></div>
          <div class="menu-row"><span>Signature Luxury Massage</span><span class="menu-price">90 mins | £72.00</span></div>
        </div>

        <div class="menu-group">
          <h2 class="menu-heading">Contemporary massage</h2>
          <p class="menu-note">Deep cleansing and ultra hydrating, our signature facials are tailor made for your skin. We focus on key stages of treatment to get you maximum results in a minimum of time.</p>
          <div class="menu-row"><span>Indian Head Massage</span><span class="menu-price">£45 | 45 mins</span></div>
          <div class="menu-row"><span>Veloura Mud massage</span><span class="menu-price">£60 | 60 mins</span></div>
          <div class="menu-row"><span>Thermal Compress massage</span><span class="menu-price">£75 | 90 mins</span></div>
        </div>

        <div class="menu-group">
          <h2 class="menu-heading">Ember Shells Massage</h2>
          <div class="menu-row"><span>Ember Shells Back Massage</span><span class="menu-price">£38 | 30 mins</span></div>
          <div class="menu-row"><span>Ember Shells Full Body Massage</span><span class="menu-price">£65 | 60 mins</span></div>
          <p class="menu-soon">COMING SOON!</p>
        </div>
      </div>
    </section>
  </main>
</body>
</html>
```